Webpage for co-working space for tech startups

We have an established co-working space in Aalborg Denmark where we have around 30 companies sharing office space. We are starting a new chapter for us and would like to have a new graphical image - new logo and new webpage, but keep the same name. The webpage should be professional, but also "fun", not too serious. We are all about working hard on our companies, but also taking some time off in between and being social and having fun. We are not corporate, but want to project the image that we are serious about what we do.

We currently have a black/red logo (see www.hivelane.dk or test.hivelane.dk), but are interesting in having a new logo design, so colour can be chosen freely. Currently our logo is a big HIVE and a little lane underneath the HIVE. The new logo will be one word "hivelane" with a small logo before or on top.

If we can make a good webpage for this project, then I have a second more simple project which is also a small single page wordpress site which I would also like to have made.

Target Market(s)

tech startups - relatively new companies, typically younger people 20-35 with a tech background - business or programming, preferably both

Industry/Entity Type

HIVE

Logo Text

hivelane

Coding

Coded - Design and coding required

Number of Pages Required

4 page

Font styles to use
Sans Serif

Colors

Designer to choose colors to be used in the design.

Requirements
Must have
• Wordpress CMS.
• Mobile and PC optimized
• 2 languages - English and Danish
• Four sections, could be four pages, or four sections of a single page.
• "Home", "Residents", "Our Working Space", "Our Event Space"
• Footer of page or pages should have contact information.
• "Home" has some information about who we are and what we do
• "Residents" has a list of all our residents - it should be possible to easily add and removed new / old residents - See one example here: http://test.hivelane.dk/en_GB/beboere/ or another example here: http://www.hivelane.dk/beboere/ - one of our colleagues http://copperyard.dk/startups/ or another one of our colleagues http://www.tidalmillhall.dk/residents/
• "Our working space" will have a description of our building, a map of where it is and a bunch of photos which show the different offices, meeting rooms and people working
• "Our events space" will have a description of our event spaces, details of cost + different arrangments of furniture, and lots of photos of events, see here for an example http://www.hivelane.dk/lej-vores-lokaler/
• Our current webpage - www.hivelane.dk was put together very quickly and has not really been optimized. We started a new webpage test.hivelane.dk, but it was never really finished.
• We are looking for a simple webpage, not too much going on. Examples of some of our colleagues in the business http://copperyard.dk/, http://www.tidalmillhall.dk/,
Nice to have
• http://www.tidalmillhall.dk/ is a really good template for us. If we can get something like this, we are happy.

```html
<!DOCTYPE html>
<html lang="en">
<head>
<meta charset="utf-8">
<title>Hivelane — Co-working space for startups</title>
<link href="https://fonts.googleapis.com/css2?family=Lato:wght@400;700;900&family=Open+Sans:wght@700&display=swap" rel="stylesheet">
<style>
:root{
  --dark:#2c2c2c;
  --darker:#222222;
  --red:#e0202e;
  --white:#ffffff;
  --light:#f3f3f3;
  --btn:#e9e9e9;
  --text:#444444;
  --muted:#bdbdbd;
}
*{margin:0;padding:0;box-sizing:border-box}
html,body{width:1200px;height:2769px;overflow:hidden}
body{position:relative;background:var(--white);font-family:'Lato',sans-serif;color:var(--text)}
.abs{position:absolute}
.hero{left:0;top:0;width:1200px;height:775px;
  background:linear-gradient(160deg,#dcdad5 0%,#c7c3bb 40%,#8a8580 75%,#5a5855 100%);
  clip-path:polygon(0 0,100% 0,100% 655px,0 775px)}
.header{left:0;top:0;width:1200px;height:122px;background:rgba(40,40,40,.78)}
.logo{left:74px;top:38px;font-weight:900;font-size:40px;color:var(--white);letter-spacing:.5px;display:flex;align-items:center;gap:12px}
.logo-mark{width:16px;height:16px;background:var(--white);display:inline-block}
.nav{left:495px;top:52px;display:flex;gap:44px;font-weight:700;font-size:13px;color:var(--white);letter-spacing:.3px}
.lang{left:1046px;top:50px;display:flex;align-items:center;gap:10px;color:var(--white);font-weight:700;font-size:13px}
.flag{width:34px;height:19px;background:linear-gradient(#b22234,#d8d8e8 50%,#b22234)}
.hero-title{left:0;width:1200px;top:312px;text-align:center;color:var(--white);font-weight:900;font-size:52px;text-shadow:0 2px 6px rgba(0,0,0,.35)}
.hero-sub{left:0;width:1200px;top:374px;text-align:center;color:var(--white);font-family:'Open Sans',sans-serif;font-weight:700;font-size:32px;line-height:38px;text-shadow:0 2px 6px rgba(0,0,0,.35)}
.photo-team{left:74px;top:618px;width:421px;height:499px;
  background:linear-gradient(135deg,#cfcfd2,#8d7f86 55%,#4c4a52);
  clip-path:polygon(0 46px,100% 0,100% calc(100% - 50px),0 100%)}
h2.section-title{font-weight:700;font-size:33px;letter-spacing:.5px}
.rule{width:114px;height:3px;background:var(--red)}
.copy{font-size:15px;line-height:26px}
.btn{display:flex;align-items:center;justify-content:center;background:var(--btn);color:#222;font-weight:700;font-size:15px;height:53px}
.who-title{left:554px;top:787px;color:#333}
.who-rule{left:554px;top:843px}
.who-copy{left:554px;top:872px;width:570px}
.who-btn{left:554px;top:1012px;width:166px}
.dark-band{left:0;top:1233px;width:1200px;height:668px;background:var(--dark);clip-path:polygon(0 0,100% 100px,100% 100%,0 100%)}
.what-title{left:74px;top:1362px;color:var(--white)}
.what-rule{left:74px;top:1416px}
.what-copy{left:74px;top:1444px;width:570px;color:#e6e6e6}
.what-btn{left:74px;top:1615px;width:166px}
.photo-hall{left:705px;top:1218px;width:421px;height:499px;
  background:linear-gradient(135deg,#e4dfd6,#a87f66 45%,#5a4a40);
  clip-path:polygon(0 0,100% 46px,100% 100%,0 calc(100% - 46px))}
.card{top:1800px;width:329px;height:242px;border:5px solid var(--white);box-shadow:0 6px 14px rgba(0,0,0,.35);display:flex;flex-direction:column;align-items:center;justify-content:center;gap:14px;color:var(--white);font-weight:900;font-size:28px;text-align:center;line-height:32px;text-shadow:0 2px 5px rgba(0,0,0,.6)}
.card-residents{left:74px;background:linear-gradient(160deg,#6d8a62,#9aa3ac 50%,#4f5a66)}
.card-working{left:436px;background:linear-gradient(160deg,#7d8a70,#5c564c 55%,#3a3632)}
.card-events{left:797px;background:linear-gradient(160deg,#6a6c70,#3e3e40 55%,#2a2a2a)}
.card svg{flex:none}
.sponsors{left:0;top:2119px;width:1200px;height:281px;background:var(--light)}
.sponsors-title{left:0;width:1200px;top:2176px;text-align:center;font-weight:700;font-size:19px;color:#333}
.sponsor{top:2236px;font-weight:700;font-size:26px;color:#2a3a5a;display:flex;align-items:center;gap:10px}
.sponsor-dot{width:18px;height:18px;border-radius:50%;background:#2a3a5a}
.footer{left:0;top:2335px;width:1200px;height:364px;background:var(--dark);clip-path:polygon(0 65px,100% 0,100% 100%,0 100%)}
.col{top:2453px;color:#e6e6e6}
.col h3{font-weight:700;font-size:18px;color:var(--white);margin-bottom:18px;letter-spacing:.3px}
.col p{font-size:13.5px;line-height:24px}
.col li{list-style:none;font-size:13.5px;line-height:33px}
.col-links{left:74px}
.col-contact{left:334px}
.col-hours{left:585px}
.col-subscribe{left:884px}
.subscribe{display:flex;margin-top:2px}
.subscribe-field{width:203px;height:40px;background:var(--white);color:#555;font-size:12px;display:flex;align-items:center;padding-left:12px}
.subscribe-go{width:39px;height:40px;background:var(--red);color:var(--white);font-weight:900;font-size:15px;display:flex;align-items:center;justify-content:center}
.social{display:flex;gap:20px;margin-top:42px;margin-left:4px}
.social span{width:18px;height:18px;border-radius:50%;background:#d8d8d8;display:block}
.bottom-bar{left:0;top:2699px;width:1200px;height:70px;background:var(--darker);display:flex;align-items:center;justify-content:center;color:#8a8a8a;font-size:12px}
</style>
</head>
<body>

<div class="abs hero" role="img" aria-label="Photo of people working at laptops in a bright open-plan office"></div>
<header class="abs header"></header>
<div class="abs logo"><span class="logo-mark"></span>HIVELANE</div>
<nav class="abs nav"><span>HOME</span><span>RESIDENTS</span><span>OUR WORKING SPACE</span><span>OUR EVENT SPACE</span></nav>
<div class="abs lang"><span class="flag" role="img" aria-label="English flag"></span>EN
  <svg width="10" height="6" viewBox="0 0 10 6"><path d="M1 1l4 4 4-4" fill="none" stroke="#fff" stroke-width="1.5"/></svg></div>
<h1 class="abs hero-title">WELCOME TO HIVELANE</h1>
<p class="abs hero-sub">We provide co-working space for<br>startup companies..</p>

<div class="abs photo-team" role="img" aria-label="Photo of a team gathered around a laptop"></div>
<h2 class="abs section-title who-title">WHO WE ARE</h2>
<div class="abs rule who-rule"></div>
<p class="abs copy who-copy">The corporate community at Hivelane is a community of tech entrepreneurs with global growth ambitions. The vision is to create the best possible conditions for North Jutland entrepreneurs by offering them an environment where they can share knowledge, experience, resources, ideas, motivation and inspiration daily.</p>
<div class="abs btn who-btn">READ MORE</div>

<div class="abs dark-band"></div>
<h2 class="abs section-title what-title">WHAT WE DO</h2>
<div class="abs rule what-rule"></div>
<p class="abs copy what-copy">Lorem ipsum dolor sit amet, consectetur adipisicing elit, sed do eiusmod tempor incididunt ut labore et doloreasdes magna aliqua. Ut enim ad minim veniam, quis nostrud exercitation ullamco laboris nisi ut aliquip ex ea commodalo consequat. Duis aute irure dolor in reprehenderit in voluptate velit esse cillum dolore eu fugiat nulla pariatur.</p>
<div class="abs btn what-btn">READ MORE</div>
<div class="abs photo-hall" role="img" aria-label="Photo of people working at wooden tables in a brick-walled hall"></div>

<div class="abs card card-residents" role="img" aria-label="Photo of the office building">RESIDENTS
  <svg width="40" height="40" viewBox="0 0 40 40"><circle cx="20" cy="20" r="20" fill="#e0202e"/><path d="M16 11l9 9-9 9" fill="none" stroke="#fff" stroke-width="4"/></svg></div>
<div class="abs card card-working" role="img" aria-label="Photo of the working space">OUR WORKING<br>SPACE
  <svg width="40" height="40" viewBox="0 0 40 40"><circle cx="20" cy="20" r="20" fill="#e0202e"/><path d="M16 11l9 9-9 9" fill="none" stroke="#fff" stroke-width="4"/></svg></div>
<div class="abs card card-events" role="img" aria-label="Photo of an event in the hall">OUR EVENTS<br>SPACE
  <svg width="40" height="40" viewBox="0 0 40 40"><circle cx="20" cy="20" r="20" fill="#e0202e"/><path d="M16 11l9 9-9 9" fill="none" stroke="#fff" stroke-width="4"/></svg></div>

<section class="abs sponsors"></section>
<h3 class="abs sponsors-title">MAIN SPONSORS</h3>
<div class="abs sponsor" style="left:98px"><span class="sponsor-dot"></span>HALVARD IP</div>
<div class="abs sponsor" style="left:370px;color:#b8531f">NORVIK</div>
<div class="abs sponsor" style="left:646px;color:#1d3a6b">Fjordsted Bank</div>
<div class="abs sponsor" style="left:900px;color:#222">ADVOKAT LUND MOE</div>

<footer class="abs footer"></footer>
<div class="abs col col-links"><h3>SITE MAP</h3>
  <ul><li>Home</li><li>Residents</li><li>Our Working Space</li><li>Our Event Space</li><li>Contact Us</li></ul></div>
<div class="abs col col-contact"><h3>CONTACT INFO</h3>
  <p>Hivelane fmba<br>Kildegade 14<br>9000 Aalborg, Denmark</p>
  <p style="margin-top:14px">(+45) 31 62 07 48</p>
  <p style="margin-top:8px">info@hivelane.dk</p></div>
<div class="abs col col-hours"><h3>OPENING HOURS</h3>
  <p>For residents: 24-7, all weekdays.</p>
  <p style="margin-top:8px">For guests: 9:00-16:00, Mon-Fri</p></div>
<div class="abs col col-subscribe"><h3>SUBSCRIBE EMAIL</h3>
  <div class="subscribe"><div class="subscribe-field">Enter Email Address</div><div class="subscribe-go">GO</div></div>
  <div class="social"><span></span><span></span><span></span><span></span><span></span></div></div>

<div class="abs bottom-bar">Copyright © 2018 Company Name All rights Reserved | Terms &amp; Conditions | Privacy</div>

</body>
</html>
```